Sightless Fellowship Hall of San Diego needs an ad/flyer for convention program

Established in 1949, the Sightless Fellowship Hall of San Diego's mission is to enrich the lives of blind and visually impaired adults by preparing them for a normal, active life in a society that is principally sighted by encouraging independence.

Located in Harwick Gardens in San Diego, California, we are a nonprofit that gives blind and visually impaired people in our community an opportunity to socialize and interact. We help members build skills, confidence, and self-esteem through our various social, recreational, and educational activities. We were founded partially by Heron Guild members and receive ongoing funding from them.

We need an 8 1/2 by 11 inch color ad in jpg format. We would like it to be editable. This will be the foundation of our rebranding. The ad will be in a meeting program of the California Herons (californiaherons.example) with the goal of highlighting some of our programs in order to solicit donations from individual Heron Guilds, preferably ongoing ones.

We would like the ad to be generic enough that we can use the ad for other events and as a flyer in the future. We want the ad/flyer to be classic but eye popping with color. We want the design to reflect a professional and lively organization that loves to serve our members. We don’t entirely love our logo, but it’s what we have for now. Our next task will be a new logo design.

We would like to highlight some of our programs for our members include bingo, blind waterskiing and surfing, cooking and ceramic classes, foreign language classes, self defense classes, yoga, and craft classes. Many of the crafts our members make are sold during fundraisers, and they include blankets, scarves, beaded animals, and more. See a sampling of pictures. We provide transportation to and from our Center, free lunch while at the Center, and food to take home. Many of these activities continue during the pandemic via online platforms. We are doing monthly home deliveries of food to our members.

We need donations to keep our programs going, and we have building repairs & maintenance that we need donations in order to complete. See attached document regarding donations. Please reach out if you have questions. Thank you.

Web address: sfhsd.example
Street address: The Sightless Fellowship Hall of San Diego, 2716 Merrow St San Diego, CA 92107
Email address: donation@sfhsd.example
To make a donation: https://sfhsd.example/donate-2/

Donors

NonProfit

Sans Serif

Must have
• Highlight programs and information on how to make a donation.
Nice to have
• Information on how much each dollar donated will go - see attachment
Should not have
• Unprofessional or sloppy details

```html
<!DOCTYPE html>
<html lang="en">
<head>
<meta charset="utf-8">
<title>Sightless Fellowship Hall of San Diego – Flyer</title>
<link rel="stylesheet" href="https://fonts.googleapis.com/css2?family=Montserrat:wght@400;500;600;700;800&display=swap">
<style>
  :root{
    --purple:#5e4a9c;
    --orange:#f7a21b;
    --teal:#45b8b5;
    --teal-deep:#17a7a1;
    --grey:#dcdcde;
    --ink:#1c1c1c;
    --white:#ffffff;
    --backdrop:#000000;
  }
  *{box-sizing:border-box;margin:0;padding:0}
  html,body{width:1200px;height:1200px;overflow:hidden;background:var(--backdrop)}
  body{font-family:"Montserrat",sans-serif;color:var(--ink);position:relative}
  .flyer{position:absolute;left:230px;top:106px;width:778px;height:1006px;background:var(--white);overflow:hidden}
  .flyer-shapes{position:absolute;left:0;top:0}
  .abs{position:absolute}
  .nowrap{white-space:nowrap}

  .intro{left:388px;top:16px;color:var(--white);font-size:12px;line-height:16px;white-space:nowrap}
  .intro strong{font-weight:700}
  .org-name{left:523px;top:196px;width:230px;font-size:28px;font-weight:700;line-height:33px;color:var(--ink)}

  .crafts-note{left:586px;top:426px;width:180px;text-align:center;font-size:14px;line-height:18px;font-weight:500;white-space:nowrap}
  .crafts-note strong{font-weight:800}

  .pill{position:absolute;color:var(--white);font-weight:800;text-transform:uppercase;display:flex;align-items:center;white-space:nowrap}
  .pill-provide{left:557px;top:621px;width:190px;height:28px;border-radius:15px;background:var(--purple);border:2px solid var(--white);justify-content:center;font-size:18px;letter-spacing:.4px}
  .provide-list{left:526px;top:663px;list-style:none}
  .provide-list li{display:flex;gap:8px;margin-bottom:8px;font-size:12px;line-height:15px;white-space:nowrap}
  .provide-list svg{flex:none;width:26px;height:22px;margin-top:2px}
  .provide-list b{font-weight:800}

  .pill-program{left:0;top:449px;width:240px;height:32px;border-radius:0 16px 16px 0;background:var(--orange);padding-left:14px;font-size:24px;letter-spacing:.3px}
  .icon-credit{left:14px;top:484px;font-size:9.5px;color:#333;white-space:nowrap}

  .program{position:absolute;width:150px;text-align:center;font-size:12px;line-height:15px;font-weight:500;text-transform:uppercase;white-space:nowrap}
  .program svg{display:block;margin:0 auto 8px;width:58px;height:58px}

  .online-note{left:239px;top:733px;width:190px;font-size:13.5px;line-height:18px;font-weight:500;white-space:nowrap}

  .pill-donation{left:0;top:848px;width:162px;height:27px;border-radius:0 14px 14px 0;background:var(--purple);padding-left:28px;font-size:19px}
  .donation-text{left:30px;top:883px;font-size:12.5px;line-height:16px;font-weight:600;white-space:nowrap}
  .donate-label{left:30px;top:926px;font-size:13px;font-weight:700;color:var(--purple);white-space:nowrap}
  .donate-bar{left:25px;top:948px;width:340px;height:40px;background:var(--orange);border-radius:4px;display:flex;align-items:center;gap:12px;padding-left:14px;font-size:15px;font-weight:700;white-space:nowrap}
  .donate-cursor{left:352px;top:958px;width:34px;height:38px}

  .contact-pin{left:740px;top:850px;width:26px;height:34px}
  .contact{right:12px;top:892px;text-align:right;color:var(--white);font-size:12.5px;line-height:16px;font-weight:700;white-space:nowrap}
  .contact .email-label{color:var(--orange)}
  .web{right:12px;top:964px;display:flex;align-items:center;gap:8px;color:var(--white);font-size:26px;font-weight:700;white-space:nowrap}
</style>
</head>
<body>
<main class="flyer">
  <svg class="flyer-shapes" viewBox="0 0 778 1006" width="778" height="1006">
    <defs>
      <linearGradient id="portrait-tone" x1="0" y1="0" x2="0" y2="1">
        <stop offset="0" stop-color="#9a8f7c"/><stop offset=".55" stop-color="#b9dccb"/><stop offset="1" stop-color="#e8ecea"/>
      </linearGradient>
      <linearGradient id="blanket-tone" x1="0" y1="0" x2="1" y2="1">
        <stop offset="0" stop-color="#8c7bb5"/><stop offset=".5" stop-color="#e7b3c8"/><stop offset="1" stop-color="#4f86b8"/>
      </linearGradient>
      <linearGradient id="figure-tone" x1="0" y1="0" x2="0" y2="1">
        <stop offset="0" stop-color="#7a7a78"/><stop offset="1" stop-color="#cfcfcf"/>
      </linearGradient>
      <linearGradient id="bead-tone" x1="0" y1="0" x2="0" y2="1">
        <stop offset="0" stop-color="#9c9c9c"/><stop offset="1" stop-color="#2d4f9c"/>
      </linearGradient>
    </defs>
    <path class="band-purple-top" d="M154 0 H778 V112 C690 150 560 160 470 145 C330 120 230 60 154 0 Z" fill="var(--purple)"/>
    <path class="band-orange-top" d="M400 148 C520 176 680 162 778 112 V140 C680 190 520 192 400 148 Z" fill="var(--orange)"/>
    <path class="band-grey-upper" d="M0 250 C120 300 260 330 400 360 L400 382 C260 354 120 322 0 274 Z" fill="var(--grey)"/>
    <path class="band-grey-side" d="M455 300 C470 360 482 420 484 480 C488 620 476 820 470 1006 H490 C496 800 506 600 500 470 C496 400 486 350 478 310 Z" fill="var(--grey)"/>
    <path class="panel-teal" d="M478 310 C560 296 680 292 778 290 V1006 H490 C496 800 506 600 500 470 C496 400 486 350 478 310 Z" fill="var(--teal)"/>
    <path class="band-orange-bottom" d="M452 1006 C455 870 590 816 778 800 V822 C600 836 480 880 480 1006 Z" fill="var(--orange)"/>
    <path class="band-purple-bottom" d="M480 1006 C480 880 600 836 778 822 V1006 Z" fill="var(--purple)"/>

    <circle cx="214" cy="222" r="205" fill="var(--teal-deep)"/>
    <circle cx="214" cy="222" r="192" fill="var(--white)"/>
    <circle cx="214" cy="222" r="186" fill="url(#portrait-tone)" role="img" aria-label="Photo of a smiling member reading braille at a library table"/>
    <circle cx="344" cy="365" r="118" fill="var(--white)"/>
    <circle cx="344" cy="365" r="112" fill="url(#blanket-tone)" role="img" aria-label="Photo of stacked hand-knitted blankets in purple, pink and blue"/>
    <circle cx="412" cy="458" r="102" fill="var(--white)"/>
    <circle cx="412" cy="458" r="96" fill="url(#figure-tone)" role="img" aria-label="Photo of a beaded holiday figure on a knitted scarf"/>
    <circle cx="508" cy="530" r="62" fill="var(--white)"/>
    <circle cx="508" cy="530" r="56" fill="url(#bead-tone)" role="img" aria-label="Photo of a beaded angel ornament"/>
  </svg>

  <p class="abs intro">We are a nonprofit that gives blind and visually impaired<br>people in our community an opportunity to socialize &amp;<br>interact. We help members build <strong>skills, confidence, and</strong><br><strong>self-esteem</strong> through our various social, recreational,<br>and educational activities.</p>

  <p class="abs org-name">Sightless<br>Fellowship Hall</p>

  <p class="abs crafts-note">Many of the crafts<br>our members make are<br><strong>SOLD DURING</strong><br><strong>FUNDRAISERS</strong><br>and they include<br>blankets, scarves,<br>beaded animals,<br>and more.</p>

  <h2 class="pill pill-provide">We Provide</h2>
  <ul class="abs provide-list">
    <li><svg viewBox="0 0 26 22"><path d="M3 11 L10 18 L23 3" fill="none" stroke="#fff" stroke-width="3.5" stroke-linecap="round" stroke-linejoin="round"/></svg><span><b>TRANSPORTATION</b><br>to &amp; from our Center</span></li>
    <li><svg viewBox="0 0 26 22"><path d="M3 11 L10 18 L23 3" fill="none" stroke="#fff" stroke-width="3.5" stroke-linecap="round" stroke-linejoin="round"/></svg><span><b>FREE LUNCH</b> while at the Center<br>and food to take home .</span></li>
    <li><svg viewBox="0 0 26 22"><path d="M3 11 L10 18 L23 3" fill="none" stroke="#fff" stroke-width="3.5" stroke-linecap="round" stroke-linejoin="round"/></svg><span>We are doing<br><b>MONTHLY HOME</b><br><b>DELIVERIES</b><br>of food to our members.</span></li>
  </ul>

  <h2 class="pill pill-program">Our Program</h2>
  <p class="abs icon-credit">Icons by Pixmoor from Iconwell.example</p>

  <div class="program" style="left:-23px;top:502px"><svg viewBox="0 0 62 62"><circle cx="33" cy="34" r="28" fill="#d0d0d0"/><circle cx="31" cy="31" r="27" fill="#f59a1f"/><rect x="20" y="19" width="22" height="24" fill="none" stroke="#fff" stroke-width="2.5"/><path d="M20 27H42M20 35H42M27 19V43M35 19V43" stroke="#fff" stroke-width="2"/></svg>Bingo</div>
  <div class="program" style="left:94px;top:502px"><svg viewBox="0 0 62 62"><circle cx="33" cy="34" r="28" fill="#d0d0d0"/><circle cx="31" cy="31" r="27" fill="#ef5a5a"/><path d="M26 44 C22 32 26 22 34 16 C38 26 36 36 30 44 Z" fill="none" stroke="#fff" stroke-width="2.5"/><path d="M18 46 Q24 42 30 46 T44 46" fill="none" stroke="#fff" stroke-width="2.5"/></svg>Blind Waterskiing<br>&amp; Surfing</div>
  <div class="program" style="left:213px;top:502px"><svg viewBox="0 0 62 62"><circle cx="33" cy="34" r="28" fill="#d0d0d0"/><circle cx="31" cy="31" r="27" fill="#d4234a"/><path d="M19 33 H43 C43 40 38 44 31 44 C24 44 19 40 19 33 Z" fill="none" stroke="#fff" stroke-width="2.5"/><circle cx="31" cy="22" r="6" fill="none" stroke="#fff" stroke-width="2.5"/></svg>Cooking</div>
  <div class="program" style="left:-23px;top:608px"><svg viewBox="0 0 62 62"><circle cx="33" cy="34" r="28" fill="#d0d0d0"/><circle cx="31" cy="31" r="27" fill="#a2187a"/><path d="M25 18 H37 C37 24 42 26 42 33 C42 40 37 44 31 44 C25 44 20 40 20 33 C20 26 25 24 25 18 Z" fill="none" stroke="#fff" stroke-width="2.5"/></svg>Ceramic<br>Classes</div>
  <div class="program" style="left:94px;top:608px"><svg viewBox="0 0 62 62"><circle cx="33" cy="34" r="28" fill="#d0d0d0"/><circle cx="31" cy="31" r="27" fill="#7a4fa0"/><circle cx="31" cy="31" r="10" fill="none" stroke="#fff" stroke-width="2.5"/><path d="M19 43 L43 19M19 19 L43 43" stroke="#fff" stroke-width="2"/></svg>Craft<br>Classes</div>
  <div class="program" style="left:213px;top:608px"><svg viewBox="0 0 62 62"><circle cx="33" cy="34" r="28" fill="#d0d0d0"/><circle cx="31" cy="31" r="27" fill="#3d8fd6"/><path d="M22 18 L40 18 L44 44 L18 44 Z" fill="none" stroke="#fff" stroke-width="2.5"/><path d="M20 30 H42" stroke="#fff" stroke-width="2.5"/></svg>Self Defense<br>Classes</div>
  <div class="program" style="left:-23px;top:722px"><svg viewBox="0 0 62 62"><circle cx="33" cy="34" r="28" fill="#d0d0d0"/><circle cx="31" cy="31" r="27" fill="#2aa44a"/><rect x="16" y="17" width="17" height="14" rx="2" fill="none" stroke="#fff" stroke-width="2.5"/><rect x="29" y="29" width="17" height="14" rx="2" fill="none" stroke="#fff" stroke-width="2.5"/></svg>Foreign<br>Language<br>Classes</div>
  <div class="program" style="left:94px;top:722px"><svg viewBox="0 0 62 62"><circle cx="33" cy="34" r="28" fill="#d0d0d0"/><circle cx="31" cy="31" r="27" fill="#7dc242"/><circle cx="31" cy="18" r="4" fill="#fff"/><path d="M31 24 V36 M20 30 L31 26 L42 30 M18 44 H44 M24 44 L31 36 L38 44" fill="none" stroke="#fff" stroke-width="2.5" stroke-linecap="round"/></svg>Yoga</div>

  <p class="abs online-note">Many of these activities<br>continue during the<br>pandemic via online<br>platforms.</p>

  <h2 class="pill pill-donation">Donation</h2>
  <p class="abs donation-text">We need donations to keep our programs going, and we have building<br>repairs &amp; maintenance that we need donations in order to complete.</p>
  <p class="abs donate-label">TO MAKE DONATIONS:</p>
  <div class="abs donate-bar">
    <svg width="22" height="22" viewBox="0 0 22 22"><circle cx="11" cy="11" r="9.5" fill="none" stroke="#fff" stroke-width="2"/><ellipse cx="11" cy="11" rx="4" ry="9.5" fill="none" stroke="#fff" stroke-width="1.6"/><path d="M1.5 11H20.5" stroke="#fff" stroke-width="1.6"/></svg>
    <span>https://sfhsd.example/donate-2/</span>
  </div>
  <svg class="abs donate-cursor" viewBox="0 0 36 40"><path d="M4 4 L32 18 L20 21 L28 34 L23 37 L15 24 L6 32 Z" fill="var(--purple)" stroke="#fff" stroke-width="2" stroke-linejoin="round"/></svg>

  <svg class="abs contact-pin" viewBox="0 0 26 34"><path d="M13 1 C6 1 1 6 1 13 C1 22 13 33 13 33 C13 33 25 22 25 13 C25 6 20 1 13 1 Z" fill="var(--orange)"/><circle cx="13" cy="13" r="5" fill="var(--purple)"/></svg>
  <p class="abs contact">The Sightless Fellowship Hall<br>of San Diego<br>2716 Merrow St San Diego, CA 92107<br><span class="email-label">EMAIL:</span> donation@sfhsd.example</p>
  <p class="abs web"><svg width="24" height="24" viewBox="0 0 22 22"><circle cx="11" cy="11" r="9.5" fill="none" stroke="#fff" stroke-width="2"/><ellipse cx="11" cy="11" rx="4" ry="9.5" fill="none" stroke="#fff" stroke-width="1.6"/><path d="M1.5 11H20.5" stroke="#fff" stroke-width="1.6"/></svg>sfhsd.example</p>
</main>
</body>
</html>
```